Filter Cleaning Business requires an advertisement that can be used on billboards, trucks, magazines

I require an advertisement that can be used wherever required promoting the services of the business in short form attracting the attention of prospective customers and making them want more information.
We also need to promote the companies philosophy to assist business improve and form partnerships in achieving this. Also that the company has proven with existing customers the ability to achieve this.
The company already has a logo and want the ad to align with the logo.

Target Market(s)

The target market is mainly Mining, Construction, Energy and Heavy Industrial companies.

Industry/Entity Type

Business

Requirements
Must have
• The ad must include the company logo
Nice to have
• The ad would include pictures of different kinds of filters serviced by the company.

```html
<!DOCTYPE html>
<html lang="en">
<head>
<meta charset="utf-8">
<title>Southern Filter Renewal Services – Advertisement</title>
<link rel="stylesheet" href="https://fonts.googleapis.com/css2?family=Open+Sans:wght@400;600&display=swap">
<style>
  :root {
    --green: #3ba54a;
    --green-deep: #2b8a3a;
    --green-dark: #1f6e2d;
    --green-light: #7cc56f;
    --white: #ffffff;
    --ink: #111111;
  }
  * { box-sizing: border-box; margin: 0; padding: 0; }
  html, body { width: 848px; height: 1200px; overflow: hidden; background: var(--white); }
  body { font-family: "Open Sans", Arial, sans-serif; }
  .ad { position: relative; width: 848px; height: 1200px; overflow: hidden; background: var(--white); }

  /* Header */
  .brand { position: absolute; left: 20px; top: 30px; width: 320px; text-align: center; }
  .brand-mark { width: 96px; height: 96px; border-radius: 50%; background: var(--green); margin: 0 auto 12px; }
  .brand-name { font-size: 17px; font-weight: 600; color: var(--green-deep); letter-spacing: 1px; line-height: 1.2; text-transform: uppercase; }
  .headline { position: absolute; left: 380px; width: 440px; text-align: center; color: var(--green); font-size: 31px; line-height: 1.4; font-weight: 400; white-space: nowrap; }
  .headline-visit { top: 30px; }
  .headline-return { top: 137px; }
  .header-rule { position: absolute; left: 0; top: 202px; width: 848px; height: 6px; background: var(--green); }

  /* Photo collage */
  .photo-strip { position: absolute; left: 0; top: 208px; width: 848px; height: 345px; background: var(--green-deep); }
  .photo { position: absolute; }
  .photo-shovel { left: 0; top: 4px; width: 449px; height: 242px; background: linear-gradient(180deg, #5a8fd0 0%, #a9c3dd 40%, #8b6a4a 75%, #6c4f36 100%); }
  .photo-pipeline { left: 453px; top: 4px; width: 395px; height: 174px; background: linear-gradient(180deg, #7d7660 0%, #b5b7b9 50%, #6e6e66 100%); }
  .photo-loader { left: 0; top: 250px; width: 470px; height: 95px; background: linear-gradient(90deg, #3b3731 0%, #8a3b2b 50%, #3a342e 100%); }
  .photo-earthworks { left: 474px; top: 182px; width: 374px; height: 163px; background: linear-gradient(180deg, #6f8f56 0%, #9b7a4e 55%, #7a5a3a 100%); }

  /* Green body */
  .body-panel { position: absolute; left: 0; top: 540px; width: 848px; height: 600px; background: radial-gradient(ellipse at 70% 60%, var(--green-light) 0%, var(--green) 45%, var(--green-deep) 100%); }
  .swoosh { position: absolute; left: 0; top: 530px; width: 848px; height: 80px; }

  .section-title { font-size: 24px; font-weight: 400; color: var(--white); line-height: 1.2; margin-bottom: 4px; }
  .feature-list { list-style: none; color: var(--white); font-size: 15.5px; line-height: 22.5px; white-space: nowrap; }
  .feature-list li { padding-left: 14px; position: relative; }
  .feature-list li::before { content: "•"; position: absolute; left: 0; }
  .services { position: absolute; left: 57px; top: 612px; width: 360px; }
  .benefits { position: absolute; left: 57px; top: 814px; width: 360px; }

  .industries { position: absolute; left: 487px; top: 592px; width: 360px; text-align: center; list-style: none; color: var(--white); font-size: 28px; line-height: 42px; text-transform: uppercase; white-space: nowrap; }

  .promise { position: absolute; left: 420px; top: 776px; width: 428px; height: 80px; }
  .promise svg { position: absolute; inset: 0; }
  .promise-text { position: absolute; left: 108px; top: 6px; width: 290px; color: var(--ink); font-size: 16px; line-height: 22px; }

  .photo-filters { position: absolute; left: 480px; top: 868px; width: 368px; height: 258px; background: radial-gradient(ellipse at 50% 55%, #e6e6e0 0%, #c9c8c0 55%, rgba(59,165,74,0) 80%); }

  .cta { position: absolute; left: 0; top: 1040px; width: 400px; height: 78px; }
  .cta svg { position: absolute; inset: 0; }
  .cta-text { position: absolute; left: 16px; top: 12px; color: var(--green); font-size: 40px; font-weight: 400; white-space: nowrap; }

  /* Footer */
  .contact { position: absolute; top: 1146px; font-size: 31px; line-height: 40px; color: var(--ink); white-space: nowrap; }
  .contact-phone { left: 10px; }
  .contact-email { left: 428px; }
</style>
</head>
<body>
<main class="ad">
  <header>
    <div class="brand">
      <div class="brand-mark"></div>
      <div class="brand-name">Southern Filter<br>Renewal Services</div>
    </div>
    <p class="headline headline-visit">We can &nbsp;come to you to<br>clean your filters!</p>
    <p class="headline headline-return">You get your filter returned!</p>
    <div class="header-rule"></div>
  </header>

  <section class="photo-strip">
    <div class="photo photo-shovel" role="img" aria-label="Large electric mining shovel at a dirt excavation site"></div>
    <div class="photo photo-pipeline" role="img" aria-label="Service utes parked beside a pipeline under construction"></div>
    <div class="photo photo-loader" role="img" aria-label="Red underground mining loader"></div>
    <div class="photo photo-earthworks" role="img" aria-label="Excavators and trucks working on an earthworks site"></div>
  </section>

  <section class="body-panel"></section>
  <svg class="swoosh" viewBox="0 0 848 80" preserveAspectRatio="none" aria-hidden="true">
    <path d="M0 20 C250 0 550 0 848 18 L848 0 L0 0 Z" fill="#2b8a3a"/>
    <path d="M0 30 C300 8 560 12 848 36 L848 26 C560 2 300 0 0 22 Z" fill="#ffffff"/>
    <path d="M0 52 C260 26 560 26 848 56 L848 48 C560 16 260 18 0 44 Z" fill="#ffffff"/>
    <path d="M0 70 C280 46 560 46 848 74 L848 70 C560 40 280 40 0 64 Z" fill="#ffffff" opacity="0.8"/>
  </svg>

  <section class="services">
    <h2 class="section-title">Services</h2>
    <ul class="feature-list">
      <li>Uses no water or chemicals</li>
      <li>Uses clean air to blow and vacuum</li>
      <li>Inspects every filter for integrity</li>
      <li>Track filter cleaning cycles</li>
      <li>Vacuum tests every filter</li>
      <li>Ironclad compliant process</li>
      <li>Provides filter test reports</li>
    </ul>
  </section>

  <section class="benefits">
    <h2 class="section-title">Benefits</h2>
    <ul class="feature-list">
      <li>Recycle</li>
      <li>Re-use</li>
      <li>Reduce landfill impact</li>
      <li>Save you 40 – 60 % off new<br>filter by recycling your filters</li>
      <li>Reduces operating expenses</li>
      <li>Increase carbon credits</li>
      <li>Reduce Inventory</li>
    </ul>
  </section>

  <ul class="industries">
    <li>Mining</li>
    <li>Energy</li>
    <li>Construction</li>
    <li>Heavy Industrial</li>
  </ul>

  <div class="promise">
    <svg viewBox="0 0 428 80" preserveAspectRatio="none" aria-hidden="true">
      <polygon points="90,0 428,0 428,80 0,80" fill="#ffffff"/>
    </svg>
    <p class="promise-text">We're confident in our company and in our product. We are sure that you will be too.</p>
  </div>

  <div class="photo-filters" role="img" aria-label="Assortment of cleaned industrial air filters"></div>

  <div class="cta">
    <svg viewBox="0 0 400 78" preserveAspectRatio="none" aria-hidden="true">
      <polygon points="0,0 400,0 340,78 0,78" fill="#ffffff"/>
    </svg>
    <p class="cta-text">Contact us today</p>
  </div>

  <footer>
    <p class="contact contact-phone">Phone: 0491570156</p>
    <p class="contact contact-email">Email: Info@sfrs.com.au</p>
  </footer>
</main>
</body>
</html>
```